Schriftfolien- und Cover-Design für Online-Video-Kurs gesucht
Zielgruppe
Ich bin Sprecher mit Medien-Produktions-Firma und suche ein neues Design für meinen Online-Video-Kurs 'Klangvoll richtig einsprechen' für Unternehmer, Podcaster, angehende Sprecher.
Ich brauche also ein Cover für die Online-Präsentation und ein Design für die Schrift-Folien, die im Video das Gesagte unterstützen, etwa wie bei einer PP-Präsentation.
Als Beispiele habe ich mein bisheriges Cover und ein Beispiel für eine Schrift-Folie angehängt.
Aufgabenstellung
Klar strukturiert, nicht zu verspielt oder verschnörkelt. Das Logo kann, muss aber nicht benutzt werden. Ebenso das Porträt-Foto.

```html
<!DOCTYPE html>
<html lang="de">
<head>
<meta charset="utf-8">
<title>Video-Crash-Kurs – Klangvoll richtig einsprechen</title>
<link href="https://fonts.googleapis.com/css2?family=Lato:wght@300;400;700&display=swap" rel="stylesheet">
<style>
  :root {
    --studio-dark: #0e0c0b;
    --studio-mid: #2a2421;
    --studio-warm: #4a3c33;
    --text-white: #ffffff;
    --text-soft: #e2e2e2;
    --accent-red: #e03a4e;
    --button-red: #b02a3a;
  }
  * { margin: 0; padding: 0; box-sizing: border-box; }
  html, body {
    width: 1200px;
    height: 462px;
    overflow: hidden;
    background: var(--studio-dark);
  }
  .cover {
    position: relative;
    width: 1200px;
    height: 462px;
    overflow: hidden;
    font-family: 'Lato', Arial, sans-serif;
    color: var(--text-white);
  }
  .studio-backdrop {
    position: absolute;
    inset: 0;
    background:
      radial-gradient(ellipse 360px 300px at 1010px 250px, #6e5a4c 0%, rgba(80,64,54,0.6) 45%, rgba(0,0,0,0) 100%),
      radial-gradient(ellipse 260px 220px at 830px 230px, rgba(120,110,100,0.35) 0%, rgba(0,0,0,0) 100%),
      radial-gradient(ellipse 400px 200px at 760px 380px, var(--studio-warm) 0%, rgba(0,0,0,0) 100%),
      linear-gradient(90deg, var(--studio-dark) 0%, #141110 45%, var(--studio-mid) 70%, #1c1816 100%);
  }
  .course-title {
    position: absolute;
    left: 45px;
    top: 30px;
    font-size: 35px;
    font-weight: 700;
    line-height: 1;
    letter-spacing: -0.3px;
  }
  .course-subtitle {
    position: absolute;
    left: 45px;
    top: 66px;
    font-size: 24px;
    font-weight: 300;
    line-height: 1;
  }
  .outline-heading {
    position: absolute;
    left: 48px;
    top: 133px;
    font-size: 23px;
    font-weight: 700;
    line-height: 1;
  }
  .outline-list {
    position: absolute;
    left: 48px;
    top: 168px;
    list-style: none;
    font-size: 13.2px;
    line-height: 25.6px;
    color: var(--text-soft);
  }
  .step-label {
    color: var(--accent-red);
    text-transform: uppercase;
  }
  .buy-button {
    position: absolute;
    left: 49px;
    top: 346px;
    width: 380px;
    height: 73px;
    border-radius: 8px;
    background: var(--button-red);
    color: var(--text-white);
    font-size: 20px;
    font-weight: 700;
    display: flex;
    align-items: center;
    justify-content: center;
    text-decoration: none;
  }
</style>
</head>
<body>
  <main class="cover">
    <div class="studio-backdrop" role="img" aria-label="Foto: Sprecher mit Kopfhörer und Studiomikrofon vor einem Mischpult im dunklen Tonstudio"></div>

    <h1 class="course-title">Video-Crash-Kurs</h1>
    <p class="course-subtitle">Klangvoll richtig einsprechen</p>

    <h2 class="outline-heading">Der Kursaufbau</h2>
    <ul class="outline-list">
      <li><span class="step-label">Equipment</span> – Sie erfahren, welches Equipment Sie sich anschaffen müssen.</li>
      <li><span class="step-label">Einleitung</span> – Ich erkläre Ihnen alles, was Sie wissen müssen.</li>
      <li><span class="step-label">Setup</span> – Nun werden Geräte und Software für die Aufnahme in Position gebracht.</li>
      <li><span class="step-label">Aufnahme</span> – Es wird ernst! – Ihre erste professionelle Aufnahme beginnt.</li>
      <li><span class="step-label">Nachbearbeitung</span> – Wie Sie die Aufnahme noch aufbereiten müssen, damit sie wirklich professionell klingt.</li>
      <li><span class="step-label">Rendering und Formate</span> – Im letzten Schritt erzeugen Sie Ihre fertige Aufnahme-Datei.</li>
    </ul>

    <a class="buy-button" href="#">Jetzt € 37-Sofort-Zugang kaufen!</a>
  </main>
</body>
</html>
```